Nonna's Ravolo

I am looking to design a label to be used on a glass jar for packaging a very special spice that has been used in our family for generations. The spice is excellent on meats, burgers, poultry, fish, and more.

The name of the spice is "Nonna's Famous Ravolo"

Design should be traditional, with an Italian feel.

Total circumference of the jar is 10"
Height of jar is 4"

Some of the glass should not be covered to reveal color of spice inside.

Target Market(s)

Female 25-75

```html
<!DOCTYPE html>
<html lang="en">
<head>
<meta charset="utf-8">
<title>Nonna's Ravolo – Label Concepts</title>
<link href="https://fonts.googleapis.com/css2?family=Playfair+Display:wght@700&display=swap" rel="stylesheet">
<style>
  :root {
    --paper: #ffffff;
    --label-red: #e30613;
    --gingham-light: #fbe3e6;
    --gingham-mid: #f2a9b3;
    --herb-green: #0b6b34;
  }
  html, body {
    margin: 0;
    padding: 0;
    overflow: hidden;
    background: var(--paper);
  }
  .canvas {
    position: relative;
    width: 1200px;
    height: 848px;
    background: var(--paper);
    overflow: hidden;
  }
  .jar-label {
    position: absolute;
    display: block;
  }
  .jar-label--top { left: 392px; top: 119px; width: 436px; height: 192px; }
  .jar-label--left { left: 55px; top: 481px; width: 415px; height: 182px; }
  .jar-label--right { left: 744px; top: 484px; width: 422px; height: 185px; }

  .band { fill: var(--label-red); }
  .gingham-field { fill: url(#ginghamTone); }
  .label-name {
    fill: var(--herb-green);
    text-anchor: middle;
    font-family: "Playfair Display", Georgia, serif;
    font-style: normal;
    font-weight: 700;
    font-size: 28px;
  }
</style>
</head>
<body>
<main class="canvas">
  <svg width="0" height="0" style="position:absolute" aria-hidden="true">
    <defs>
      <linearGradient id="ginghamTone" x1="0" y1="0" x2="1" y2="1">
        <stop offset="0" stop-color="#f4b3bc"/>
        <stop offset="0.5" stop-color="#fbe3e6"/>
        <stop offset="1" stop-color="#f2a9b3"/>
      </linearGradient>
    </defs>
  </svg>

  <svg class="jar-label jar-label--top" viewBox="0 0 309 136">
    <rect class="gingham-field" x="0" y="7" width="309" height="120" role="img" aria-label="Red and white gingham check pattern"/>
    <rect class="band" x="0" y="0" width="309" height="7"/>
    <rect class="band" x="0" y="127" width="309" height="9"/>
    <text class="label-name" x="154.5" y="63">Nonna’s</text>
    <text class="label-name" x="154.5" y="97">Ravolo</text>
  </svg>

  <svg class="jar-label jar-label--left" viewBox="0 0 294 129">
    <rect class="gingham-field" x="0" y="7" width="294" height="114" role="img" aria-label="Red and white gingham check pattern"/>
    <rect class="band" x="0" y="0" width="294" height="7"/>
    <rect class="band" x="0" y="121" width="294" height="8"/>
    <text class="label-name" x="147" y="60">Nonna’s</text>
    <text class="label-name" x="147" y="94">Ravolo</text>
  </svg>

  <svg class="jar-label jar-label--right" viewBox="0 0 299 131">
    <rect class="gingham-field" x="0" y="7" width="299" height="115" role="img" aria-label="Red and white gingham check pattern"/>
    <rect class="band" x="0" y="0" width="299" height="7"/>
    <rect class="band" x="0" y="122" width="299" height="9"/>
    <text class="label-name" x="149.5" y="61">Nonna’s</text>
    <text class="label-name" x="149.5" y="95">Ravolo</text>
  </svg>
</main>
</body>
</html>
```